Redesign of outdated "Automotive Automation Company"

We are looking to finally update our outdated website with some cutting edge graphics. We want our customers to know we value technology and are cutting edge as far as design. We provide automation solutions for the automotive industry which essentially means we program robots, and sell automation related products.

Current URL

http://lnk.vexor.test/Qm7trz
Updates

Project Deadline Extended
Reason: The client portal wasn't working, it's just finally been fixed by Pixel Harbor. I will go through and start reviewing designs.

We are trying to go with the same look and feel on our business cards, line cards, apparel, etc. so we are forming a brand. I have included the current draft of the line card. Please utilize our newest Logo TMV Standardized Logo.jpg http://img.pelvarhost.test/zq4Rb8d.jpg?1 Also we are trying hard to sell the following software / hardware companies so we can put some emphasis on their product. Corvane Systems https://www.corvanesystems.test/ We make money on selling the software and then on the integration. I think you should tie in this animation. ยท Shop Line Tangle to Throughput https://media.vidloft.test/deliveries/9b2e7c41d05f83a6c17e2d94b0a6f3e1c85d7b42.jpg?image_play_button=true&image_play_button_color=7b796ae0&image_crop_resized=275x155 In this 2-minute video, discover how Keystroke can help run your plant floor. We are Authorized Integrators / Resellers for Halbrook Controls Tavrin Sensorik http://tavrin.test/en/usa/ Corvane Systems https://www.corvanesystems.test/ Meridel Process Works www.mpwxx.test Solbry Belt Corp www.solbrybelt.test Quellmark Fabrication http://www.quellmarkfab.test/strategic_partners.aspx

Target Market(s)

Large automotive companies looking for automation or robotic programming. So Professional is key.

Industry/Entity Type

Automotive

Font styles to use
Other font styles liked:
• Possible Open Sans or Lato

Colors
0591cc
ceeaf6
fbd4d5
fbf289
fece3e

Requirements
Must have
• Professional Modern Design.

I want a homepage design, and a rough Sales Page... Where numerous products can be listed.
Nice to have
• Maybe an updated logo if possible.

```html
<!DOCTYPE html>
<html lang="en">
<head>
<meta charset="utf-8">
<title>TMV Engineering Solutions</title>
<link href="https://fonts.googleapis.com/css2?family=Arimo:wght@400;700&family=Jost:wght@300;400;500;600&display=swap" rel="stylesheet">
<style>
:root{
  --page:#ffffff;
  --header-bg:#f3f3f3;
  --ink:#222222;
  --muted:#444444;
  --navy:#1a4a7a;
  --blue:#1c6fb0;
  --blue-deep:#0d4f8f;
  --gold:#f4b71e;
  --rose:#c8264b;
  --grey-band:#e6e6e6;
  --footer:#2b2b2b;
  --footer-text:#e8e8e8;
  --accent-red:#e0264a;
}
*{margin:0;padding:0;box-sizing:border-box}
html,body{width:690px;height:1200px;overflow:hidden;background:var(--page)}
body{font-family:"Arimo",Arial,sans-serif;color:var(--ink);position:relative}
.abs{position:absolute}

/* header */
.site-header{position:absolute;left:0;top:0;width:690px;height:83px;background:var(--header-bg)}
.brand{position:absolute;left:58px;top:26px;display:flex;align-items:center;gap:6px}
.brand-mark{width:14px;height:14px;border-radius:50%;background:var(--accent-red)}
.brand-name{font-family:"Jost",sans-serif;font-weight:600;font-size:12px;color:var(--navy);line-height:1.15;width:92px}
.social{position:absolute;left:510px;top:12px;display:flex;gap:9px}
.social span{width:11px;height:11px;border-radius:50%;background:#8a8a8a}
.contact-phone{position:absolute;right:66px;top:34px;font-size:7.5px;color:#555}
.contact-phone b{font-weight:400;color:var(--blue-deep)}
.main-nav{position:absolute;left:296px;top:60px;width:292px;height:30px;display:flex;border-radius:4px;overflow:hidden;background:linear-gradient(#fafafa,#e2e2e2);box-shadow:0 1px 2px rgba(0,0,0,.25)}
.main-nav a{flex:1;display:flex;align-items:center;justify-content:center;font-family:"Jost",sans-serif;font-weight:300;font-size:10px;color:#333;text-decoration:none;border-right:1px solid #d0d0d0}
.main-nav a:last-child{border-right:0}
.main-nav a.is-current{background:linear-gradient(#e4e4e4,#d2d2d2)}

/* hero */
.hero{position:absolute;left:0;top:83px;width:690px;height:261px;background:linear-gradient(115deg,#0b4d8c 0%,#1a6db0 45%,#2c86c8 75%,#1f6eb0 100%)}
.hero-figure{position:absolute;left:88px;top:8px;width:196px;height:250px;border-radius:40px 40px 10px 10px;background:radial-gradient(ellipse at 45% 40%,#f2f4f6 0%,#c9ced4 55%,rgba(120,140,160,.0) 80%)}
.hero-title{position:absolute;left:293px;top:60px;font-family:"Jost",sans-serif;font-weight:600;font-size:24.5px;color:#fff;letter-spacing:.3px}
.hero-text{position:absolute;left:293px;top:97px;width:330px;font-size:7.6px;line-height:14.4px;color:#eef4fb}

/* intro */
.intro-title{position:absolute;left:0;top:360px;width:690px;text-align:center;font-size:17px;color:#2a2a2a}
.intro-sub{position:absolute;left:0;top:386px;width:690px;text-align:center;font-size:12px;color:var(--gold)}
.intro-rule{position:absolute;left:123px;top:407px;width:439px;height:1px;background:#cfcfcf}
.intro-text{position:absolute;left:58px;top:415px;width:574px;text-align:center;font-size:7.6px;line-height:17px;color:#333}

/* feature cards */
.card{position:absolute;top:500px;width:164px;height:108px;border:2px solid #bdbdbd}
.card-visual{position:absolute;inset:0}
.card-caption{position:absolute;left:0;bottom:4px;width:136px;height:18px;padding-left:6px;display:flex;align-items:center;background:var(--blue-deep);font-family:"Jost",sans-serif;font-weight:500;font-size:8px;color:#fff}
.card--team{left:70px}
.card--team .card-visual{background:linear-gradient(180deg,#dfe6ee,#8fa6bf)}
.card--plan{left:262px}
.card--plan .card-visual{background:linear-gradient(180deg,#3d72b8,#1e4f95)}
.card--ideas{left:455px}
.card--ideas .card-visual{background:linear-gradient(160deg,#f1f3f6,#c4ccd6)}

/* overview */
.overview{position:absolute;left:0;top:643px;width:690px;height:262px;background:var(--grey-band)}
.overview-title{position:absolute;left:0;top:14px;width:690px;text-align:center;font-size:25px;color:var(--navy);letter-spacing:.5px}
.overview-rule{position:absolute;left:247px;top:44px;width:197px;height:1px;background:#a64a5a}
.service-icon{position:absolute;width:47px;height:47px}
.service-title{position:absolute;font-size:10.6px;color:#333;letter-spacing:.2px}
.service-text{position:absolute;width:206px;font-size:7.8px;line-height:13px;color:#333}

/* specialties */
.spec-title{position:absolute;left:0;top:922px;width:690px;text-align:center;font-size:12.6px;color:var(--navy)}
.spec-rule{position:absolute;left:215px;top:942px;width:289px;height:1px;background:var(--accent-red)}
.spec-list{position:absolute;top:960px;list-style:none}
.spec-list li{height:23.4px;display:flex;align-items:center;gap:8px;font-size:8px;color:#222}
.spec-list svg{width:10px;height:10px;flex:none}

/* footer */
.site-footer{position:absolute;left:0;top:1100px;width:690px;height:100px;background:var(--footer);border-top:3px solid var(--accent-red)}
.footer-address{position:absolute;left:66px;top:8px;font-size:7.6px;line-height:13.6px;color:var(--footer-text)}
.footer-brand{position:absolute;left:545px;top:25px;display:flex;align-items:center;gap:5px}
.footer-brand .brand-mark{width:10px;height:10px}
.footer-brand span{font-family:"Jost",sans-serif;font-weight:600;font-size:9px;color:#ddd;width:80px;line-height:1.15}
.footer-rule{position:absolute;left:58px;top:70px;width:574px;height:1px;background:#444}
.footer-nav{position:absolute;left:0;top:80px;width:690px;text-align:center;font-size:7.4px;color:#ddd}
.footer-nav a{color:#ddd;text-decoration:none}
.footer-nav i{font-style:normal;margin:0 10px}
</style>
</head>
<body>

<header class="site-header">
  <div class="brand"><span class="brand-mark"></span><span class="brand-name">TMV Engineering Solutions</span></div>
  <div class="social" aria-label="Social links"><span></span><span></span><span></span><span></span><span></span><span></span></div>
  <p class="contact-phone">Contact Phone: <b>+123 555 0190</b></p>
  <nav class="main-nav">
    <a href="#" class="is-current">Home Page</a><a href="#">Services</a><a href="#">Contact</a><a href="#">About</a>
  </nav>
</header>

<section class="hero">
  <div class="hero-figure" role="img" aria-label="White humanoid service robot gesturing toward the headline"></div>
  <h1 class="hero-title">TMV ENGINEERING SOLUTIONS</h1>
  <p class="hero-text">Lorem ipsum dolor sit amet, consectetur adipiscing elit, sed do eiusmod tempor incididunt ut labore et dolore magna aliqua. Ut &nbsp;proident, sunt in culpa qui officia deserunt mollit anim id est laborum.</p>
</section>

<h2 class="intro-title">Your Premier Automation Consulting &amp; Systems Integration choice!</h2>
<p class="intro-sub">Helping your business optimize its Automation....</p>
<div class="intro-rule"></div>
<p class="intro-text">Lorem ipsum dolor sit amet, consectetur adipiscing elit, sed do eiusmod tempor incididunt ut labore et dolore magna aliqua. Ut enim ad minim veniam, quis nostrud exercitation ullamco laboris nisi ut aliquip ex ea commodo consequat. Duis aute irure dolor in reprehenderit in voluptate velit esse cillum dolore eu fugiat nulla pariatur. Excepteur sint occaecat cupidatat non proident, sunt in culpa qui officia deserunt mollit anim id est laborum.</p>

<a class="card card--team" href="#"><div class="card-visual" role="img" aria-label="Business team silhouettes in front of a world map"></div><span class="card-caption">Get to know our Team approach</span></a>
<a class="card card--plan" href="#"><div class="card-visual" role="img" aria-label="Businessman facing a chalkboard of strategy sketches"></div><span class="card-caption">This way to Automation success</span></a>
<a class="card card--ideas" href="#"><div class="card-visual" role="img" aria-label="Hands reviewing paperwork with a pen"></div><span class="card-caption">Bring great ideas to your business</span></a>

<section class="overview">
  <h2 class="overview-title">OVERVIEW</h2>
  <div class="overview-rule"></div>

  <svg class="service-icon" style="left:63px;top:71px" viewBox="0 0 48 48" aria-hidden="true">
    <circle cx="24" cy="24" r="22.5" fill="#fff" stroke="#111" stroke-width="1.5"/>
    <circle cx="20" cy="21" r="6" fill="none" stroke="#111" stroke-width="3.5" stroke-dasharray="2.4 1.6"/>
    <circle cx="20" cy="21" r="2" fill="#111"/>
    <circle cx="29" cy="29" r="4" fill="none" stroke="#111" stroke-width="2.8" stroke-dasharray="1.8 1.4"/>
  </svg>
  <h3 class="service-title" style="left:123px;top:75px">APPLICATIONS ENGINEERING</h3>
  <p class="service-text" style="left:123px;top:91px">Provide electrical and mechanical expertise to solve automation specific application problems by utilizing best known industry practices.</p>

  <svg class="service-icon" style="left:368px;top:71px" viewBox="0 0 48 48" aria-hidden="true">
    <circle cx="24" cy="24" r="22.5" fill="#fff" stroke="#111" stroke-width="1.5"/>
    <path d="M16 14 L34 32" stroke="#111" stroke-width="5" stroke-linecap="round"/>
    <path d="M32 14 L16 32" stroke="#111" stroke-width="3" stroke-linecap="round"/>
  </svg>
  <h3 class="service-title" style="left:428px;top:75px">DESIGN ENGINEERING</h3>
  <p class="service-text" style="left:428px;top:91px">Provide electro-mechanical designs for machine down-time improvements and cost reductions. Perform sizing calculations for motion control and fluid power applica-tions.</p>

  <svg class="service-icon" style="left:63px;top:163px" viewBox="0 0 48 48" aria-hidden="true">
    <circle cx="24" cy="24" r="22.5" fill="#fff" stroke="#111" stroke-width="1.5"/>
    <g fill="none" stroke="#111" stroke-width="2.2">
      <circle cx="24" cy="19" r="7.5"/><circle cx="19.5" cy="27" r="7.5"/><circle cx="28.5" cy="27" r="7.5"/>
    </g>
  </svg>
  <h3 class="service-title" style="left:123px;top:167px">DESIGN SPECIFICATION</h3>
  <p class="service-text" style="left:123px;top:183px">Develop controls and mechanical specifications for ma-chines to be used when purchasing equipment. Collabo-rate with the systems integrator / machine OEM to ensure adherence to machine specifications.</p>

  <svg class="service-icon" style="left:368px;top:167px" viewBox="0 0 48 48" aria-hidden="true">
    <circle cx="24" cy="24" r="22.5" fill="#fff" stroke="#111" stroke-width="1.5"/>
    <path d="M27 12 L18 26 H24 L21 36 L31 21 H25 Z" fill="#111"/>
    <g stroke="#111" stroke-width="1.6" stroke-linecap="round">
      <path d="M11 24 H14"/><path d="M34 24 H37"/><path d="M15 15 L17 17"/><path d="M31 31 L33 33"/><path d="M15 33 L17 31"/><path d="M31 17 L33 15"/>
    </g>
  </svg>
  <h3 class="service-title" style="left:431px;top:171px">ELECTRICAL ENGINEERING</h3>
  <p class="service-text" style="left:431px;top:187px">Provide electro-mechanical designs for machine down-time improvements and cost reductions. Perform sizing calculations for motion control and fluid power applica-tions.</p>
</section>

<h2 class="spec-title">SPECIALIZING IN THE FOLLOWING AREAS</h2>
<div class="spec-rule"></div>

<svg width="0" height="0" style="position:absolute">
  <symbol id="tick-box" viewBox="0 0 10 10"><rect x="0.7" y="1.2" width="8" height="7.6" rx="1.2" fill="none" stroke="#d0284d" stroke-width="1.1"/><path d="M2.6 5 L4.4 6.8 L9.2 1.6" fill="none" stroke="#d0284d" stroke-width="1.2"/></symbol>
</svg>

<ul class="spec-list" style="left:60px">
  <li><svg><use href="#tick-box"/></svg>2D and 3D Capabilities</li>
  <li><svg><use href="#tick-box"/></svg>HMI Programming</li>
  <li><svg><use href="#tick-box"/></svg>Industrial Networks / Fieldbus</li>
  <li><svg><use href="#tick-box"/></svg>Industrial Network Security</li>
  <li><svg><use href="#tick-box"/></svg>Contract Engineering /Techs</li>
</ul>
<ul class="spec-list" style="left:284px">
  <li><svg><use href="#tick-box"/></svg>2D and 3D Capabilities</li>
  <li><svg><use href="#tick-box"/></svg>HMI Programming</li>
  <li><svg><use href="#tick-box"/></svg>Industrial Networks / Fieldbus</li>
  <li><svg><use href="#tick-box"/></svg>Industrial Network Security</li>
  <li><svg><use href="#tick-box"/></svg>Contract Engineering /Techs</li>
</ul>
<ul class="spec-list" style="left:497px">
  <li><svg><use href="#tick-box"/></svg>2D and 3D Capabilities</li>
  <li><svg><use href="#tick-box"/></svg>HMI Programming</li>
  <li><svg><use href="#tick-box"/></svg>Industrial Networks / Fieldbus</li>
  <li><svg><use href="#tick-box"/></svg>Industrial Network Security</li>
  <li><svg><use href="#tick-box"/></svg>Contract Engineering /Techs</li>
</ul>

<footer class="site-footer">
  <address class="footer-address" style="font-style:normal">www.TmvEngSolutions.test<br>402 W. Lattice Road<br>PO Box 318<br>Dunmore, MI 48011</address>
  <div class="footer-brand"><span class="brand-mark"></span><span>TMV Engineering Solutions</span></div>
  <div class="footer-rule"></div>
  <nav class="footer-nav"><a href="#">Home Page</a><i>|</i><a href="#">Services</a><i>|</i><a href="#">Contact</a><i>|</i><a href="#">About</a></nav>
</footer>

</body>
</html>
```